Velmaric Business Card Design

We need to update our current company business cards to something that is more professional. We are oilfield equipment manufacturing company. The company has and will continue to use a logo that is similar to the TORVEN aspirin logo. I would like to see that used alone in the design because that is how most companies recognize us. I also would not mind seeing the logo designed into something more "oilfield" to add some identification to our product line (i.e. maybe a oil rig coming off of it or something). Our units are primarily red, so I would like to stick with a red, black, white, and maybe grey color scheme. In addition to our logo. Our QDL logo should be on back of card similar to the one I am attaching (PRUETTS). I am in process of getting a clean copy of that image. I am attaching a card (PRUETTS) from a previous company that I worked at that is now closed that I like the design of. I have also attached a current business card.
Updates

I have added our logo and an old business card from a company no longer in existence that I really like the design of. Please use those items in design and a color scheme of red and black. Grey and white can also be incorporated if needed. I need a design that will also translate easily to letterhead, brochures, documents, etc. I plan on also having those designed when I find the right designer.

Industry/Entity Type

Business

Contact Information for Business Card

Front

Velmaric Services (and logo)

Marisa Kolb
Management Rep

361-574-8062 Phone
361-574-8069 Fax
361-730-4486 Mobile
mkolb@velmaricrigworks.example

Back:
Corpus Christi - Headquarters
4190 Sandpiper St.
Corpus Christi, TX 78452

Texas - North Dakota - Pennsylvania

www.velmaricrigworks.example

Colors
ec2027
000000
5c5c5c
ffffff

Requirements
Nice to have
• The owners do like cards that have an expensive look to them. They feel that they have achieved that previously with raised ink. That feature or something that separates this card from other would be nice.
Should not have
• This card should not be SUPER modern. This is still an "old school" type owned company. The card should be professional thou.

```html
<!DOCTYPE html>
<html lang="en">
<head>
<meta charset="utf-8">
<title>Velmaric Services – Business Card</title>
<link rel="stylesheet" href="https://fonts.googleapis.com/css2?family=Arimo:wght@700&family=Open+Sans:wght@400;600&display=swap">
<style>
  :root {
    --red: #ec2027;
    --red-deep: #a80f14;
    --black: #000000;
    --grey: #5c5c5c;
    --white: #ffffff;
    --backdrop: #e9e7e4;
    --ink: #1a1a1a;
  }
  * { margin: 0; padding: 0; box-sizing: border-box; }
  html, body { width: 1200px; height: 494px; overflow: hidden; }
  body {
    position: relative;
    background: var(--backdrop);
    font-family: "Open Sans", Arial, sans-serif;
    color: var(--ink);
  }

  /* ---------- Front card ---------- */
  .card-front {
    position: absolute; left: 36px; top: 30px;
    width: 556px; height: 316px;
    background: var(--white);
    box-shadow: 0 4px 14px rgba(0,0,0,.25);
  }
  .name-band {
    position: absolute; left: 0; top: 0; width: 100%; height: 36px;
    background: var(--black); color: var(--white);
    display: flex; align-items: center; justify-content: center;
    font-size: 17px; font-weight: 600;
  }
  .name-band .title { font-size: 13px; font-weight: 400; margin-left: 5px; }
  .rule-pair { position: absolute; left: 0; width: 100%; }
  .rule-pair::before, .rule-pair::after { content: ""; display: block; width: 100%; }
  .rule-pair::before { height: 3px; background: var(--red); }
  .rule-pair::after { height: 1px; background: var(--grey); margin-top: 3px; opacity: .6; }
  .rule-top { top: 40px; }
  .rule-bottom { top: 272px; }

  .brand-front {
    position: absolute; left: 0; top: 80px; width: 100%; height: 60px;
    display: flex; align-items: center; justify-content: center; gap: 12px;
    font-family: "Arimo", Arial, sans-serif; font-weight: 700;
    font-size: 28px; color: var(--red); letter-spacing: 1px;
  }
  .brand-front .mark-circle {
    width: 56px; height: 56px; border: 5px solid var(--red); border-radius: 50%;
  }
  .company-name {
    position: absolute; left: 0; top: 160px; width: 100%; text-align: center;
    font-family: "Arimo", Arial, sans-serif; font-weight: 700;
    font-size: 30px; line-height: 36px; color: var(--red); letter-spacing: .5px;
  }
  .contact-row {
    position: absolute; left: 0; width: 100%;
    display: flex; justify-content: center; gap: 18px;
    font-size: 14px; line-height: 20px; color: var(--ink);
  }
  .contact-row.phones { top: 222px; }
  .contact-row.online { top: 245px; }
  .contact-item { display: flex; align-items: center; gap: 6px; white-space: nowrap; }
  .contact-item svg { width: 13px; height: 13px; fill: var(--ink); }

  .address-band {
    position: absolute; left: 0; bottom: 0; width: 100%; height: 34px;
    background: var(--black); color: var(--white);
    display: flex; align-items: center; justify-content: center;
    font-size: 14px;
  }

  /* ---------- Back card ---------- */
  .card-back {
    position: absolute; left: 618px; top: 146px;
    width: 552px; height: 318px;
    background: radial-gradient(ellipse at 45% 45%, var(--red) 0%, #c4141a 55%, var(--red-deep) 100%);
    box-shadow: 0 4px 14px rgba(0,0,0,.25);
  }
  .brand-back {
    position: absolute; left: 0; top: 84px; width: 100%; height: 96px;
    display: flex; align-items: center; justify-content: center; gap: 18px;
    font-family: "Arimo", Arial, sans-serif; font-weight: 700;
    font-size: 46px; color: var(--white); letter-spacing: 2px;
  }
  .brand-back .mark-circle {
    width: 90px; height: 90px; border: 8px solid var(--white); border-radius: 50%;
  }
  .website-back {
    position: absolute; left: 0; top: 268px; width: 100%; text-align: center;
    font-size: 14px; color: var(--white); letter-spacing: 2px;
  }
</style>
</head>
<body>

<section class="card-front" aria-label="Business card front">
  <div class="name-band">Your Name,<span class="title">Title</span></div>
  <div class="rule-pair rule-top"></div>

  <div class="brand-front"><span class="mark-circle"></span>VELMARIC</div>
  <div class="company-name">VELMARIC SERVICES</div>

  <div class="contact-row phones">
    <span class="contact-item">
      <svg viewBox="0 0 16 16" aria-hidden="true"><path d="M3.6 1.2l2.3 2.8-1.4 1.8c.9 2.1 2.6 3.8 4.7 4.7l1.8-1.4 2.8 2.3-1.5 2.4C7 13.6 2.4 9 1.2 3.1z"/></svg>
      555 014 8062
    </span>
    <span class="contact-item">
      <svg viewBox="0 0 16 16" aria-hidden="true"><path d="M4.5 0h7v16h-7zM6 2v10h4V2zm1.2 11.2v1.4h1.6v-1.4z"/></svg>
      555 014 4486
    </span>
    <span class="contact-item">
      <svg viewBox="0 0 16 16" aria-hidden="true"><path d="M4 1h8v4h3v8H1V5h3zm1.5 1.5V5h5V2.5zM3 8v1.5h10V8z"/></svg>
      555 014 8069
    </span>
  </div>

  <div class="contact-row online">
    <span class="contact-item">
      <svg viewBox="0 0 16 16" aria-hidden="true"><path d="M1 5l7-4 7 4v9H1zm1.5 1.2L8 10l5.5-3.8V5.8L8 2.7 2.5 5.8z"/></svg>
      mkolb@velmaricrigworks.example
    </span>
    <span class="contact-item">
      <svg viewBox="0 0 16 16" aria-hidden="true"><path d="M8 0a8 8 0 100 16A8 8 0 008 0zm0 1.5c.9 0 1.9 1.8 2.2 4.5H5.8C6.1 3.3 7.1 1.5 8 1.5zM5.7 7.5h4.6a13 13 0 010 1H5.7a13 13 0 010-1zM1.6 7.5h2.6v1H1.6zm10.2 0h2.6v1h-2.6zM5.8 10h4.4c-.3 2.7-1.3 4.5-2.2 4.5S6.1 12.7 5.8 10z"/></svg>
      www.velmaricrigworks.example
    </span>
  </div>

  <div class="rule-pair rule-bottom"></div>
  <div class="address-band">Street Name, City Name, Zip Code-00000</div>
</section>

<section class="card-back" aria-label="Business card back">
  <div class="brand-back"><span class="mark-circle"></span>VELMARIC</div>
  <div class="website-back">www.velmaricrigworks.example</div>
</section>

</body>
</html>
```